Penny Parcel Ad

I need to create a layout with the information on the PDF, but I want you to re-design it and freshen up the look. I've attached a Word Doc with the size and format requirement for the penny parcel print. The PDF I created in illustrator CS6 also has the proper guides.

Target Market(s)

Storm Damaged Areas

Font styles to use
Serif
Sans Serif

Requirements
Must have
• Fresh, clean design. I prefer upscale look versus modern or techy.

```html
<!DOCTYPE html>
<html lang="en">
<head>
<meta charset="utf-8">
<title>Fair Hands Roofing – Penny Parcel Ad</title>
<link href="https://fonts.googleapis.com/css2?family=Oswald:wght@500;700&family=Ubuntu:wght@700&family=Fira+Sans+Condensed:wght@500;600&family=Nunito+Sans:wght@400&family=Roboto+Slab:wght@500&display=swap" rel="stylesheet">
<style>
  :root {
    --brick: #b53c31;
    --brick-dark: #a4342a;
    --brown: #3a1f17;
    --orange: #e8732a;
    --gold: #f6b84b;
    --coupon: #f5ee72;
    --ink: #222;
    --grey: #3c3c3c;
    --white: #fff;
    --tan: #f2cf8c;
  }
  * { margin: 0; padding: 0; box-sizing: border-box; }
  html, body { width: 1200px; height: 782px; overflow: hidden; background: var(--white); }
  .ad { position: relative; width: 1200px; height: 782px; background: var(--white); font-family: "Nunito Sans", sans-serif; color: var(--ink); }

  .brand { position: absolute; left: 48px; top: 40px; display: flex; align-items: center; gap: 14px; }
  .brand-dot { width: 80px; height: 80px; border-radius: 50%; background: var(--brown); }
  .brand-name { font-family: "Oswald", sans-serif; font-weight: 700; font-size: 72px; line-height: 1; color: var(--brown); letter-spacing: -1px; }

  .quote-cta { position: absolute; right: 46px; top: 30px; text-align: right; }
  .quote-cta h1 { font-family: "Oswald", sans-serif; font-weight: 700; font-size: 54px; line-height: 1.1; color: var(--brick); letter-spacing: 0.5px; }
  .quote-url { font-family: "Ubuntu", sans-serif; font-weight: 700; font-size: 34px; color: var(--grey); line-height: 1.1; }
  .quote-url span { color: var(--orange); }

  .band { position: absolute; left: 0; top: 163px; width: 1200px; height: 308px; background: var(--brick); }
  .coupon { position: absolute; top: 27px; width: 246px; height: 172px; background: linear-gradient(90deg, #c94a1a, #f08a2a 10%, #f08a2a 90%, #c94a1a); padding: 10px 10px 14px; }
  .coupon-inner { width: 100%; height: 100%; background: var(--coupon); font-family: "Roboto Slab", serif; font-weight: 500; font-size: 21px; color: var(--brick); padding-top: 12px; padding-left: 52px; }
  .c1 { left: 51px; } .c2 { left: 334px; } .c3 { left: 615px; } .c4 { left: 901px; }

  .feature { position: absolute; top: 232px; color: var(--white); }
  .feature h2 { font-family: "Fira Sans Condensed", sans-serif; font-weight: 600; font-size: 20px; color: var(--gold); text-transform: uppercase; margin-bottom: 4px; }
  .feature p { font-size: 17px; line-height: 22px; }
  .f1 { left: 46px; } .f2 { left: 414px; } .f3 { left: 752px; }

  .reviews-title { position: absolute; left: 47px; top: 494px; font-family: "Roboto Slab", serif; font-weight: 500; font-size: 21px; color: var(--brick); }
  .review { position: absolute; left: 47px; top: 530px; width: 624px; font-size: 14.6px; line-height: 19.2px; text-align: justify; }
  .review cite { font-style: normal; font-family: "Roboto Slab", serif; font-weight: 500; font-size: 17px; color: var(--orange); margin-left: 14px; }

  .local-title { position: absolute; left: 694px; top: 494px; font-family: "Fira Sans Condensed", sans-serif; font-weight: 500; font-size: 24px; color: var(--brick); }
  .roofer-art { position: absolute; left: 760px; top: 525px; }
  .partner { position: absolute; left: 699px; top: 548px; display: flex; align-items: center; gap: 14px; }
  .partner-badge { width: 52px; height: 52px; background: var(--brick); }
  .partner-label { font-family: "Oswald", sans-serif; font-weight: 500; font-size: 29px; line-height: 31px; color: var(--brown); }

  .call { position: absolute; left: 47px; top: 696px; font-family: "Oswald", sans-serif; font-weight: 700; color: var(--brick); display: flex; align-items: baseline; gap: 10px; }
  .call-label { font-size: 38px; }
  .call-number { font-size: 62px; color: var(--orange); line-height: 1; }
  .accredit-badge { position: absolute; left: 536px; top: 702px; width: 163px; height: 61px; background: #111; border-radius: 6px; }
  .rating-badge { position: absolute; left: 788px; top: 706px; width: 48px; height: 48px; border-radius: 50%; background: #111; }
</style>
</head>
<body>
<div class="ad">
  <div class="brand"><span class="brand-dot"></span><span class="brand-name">Fair Hands</span></div>

  <div class="quote-cta">
    <h1>Get a ROOF Quote Online!</h1>
    <div class="quote-url">www.fairhandsgc.com/<span>roofquote</span></div>
  </div>

  <section class="band">
    <div class="coupon c1"><div class="coupon-inner">Coupon #1</div></div>
    <div class="coupon c2"><div class="coupon-inner">Coupon #2</div></div>
    <div class="coupon c3"><div class="coupon-inner">Coupon #3</div></div>
    <div class="coupon c4"><div class="coupon-inner">Coupon #4</div></div>

    <div class="feature f1"><h2>Fully Insured Roofing Crews</h2><p>We carry both Liability Coverage and<br>Workers Compensation for our crews.</p></div>
    <div class="feature f2"><h2>Quality, Hand Nailed Roofs</h2><p>Ask about our professional<br>installation process.</p></div>
    <div class="feature f3"><h2>Licensed Texas Property Adjusters</h2><p>We have experience adjusting claims &amp; will<br>help you close your claim quickly.</p></div>
  </section>

  <h3 class="reviews-title">See what your neighbours in North Texas are saying about us.</h3>
  <p class="review">I am a very skeptical person when it caes to genera contracting and particulary roofing. Fair Hands put the roof on my mother-in-laws house after the bad hail storm we had. Ray was at the work site about 90% of the time making sure he was available to not ony the crew, but to my mother-in-law as well. He warked well with insurance adjuster and made sure all the paperwork was in order for the insurance company AND the bank. You just don't see service like that often. He went on to do my neighbours house as well. Both jos were done professionally and looked amazing. As long as Fair Hands os in business, I will continue to refer and use them.<cite>Marcus T - Granbury, TX</cite></p>

  <h3 class="local-title">Locally Owned Company Servicing North Texas</h3>
  <svg class="roofer-art" width="440" height="257" viewBox="0 0 440 257" role="img" aria-label="Cartoon roofer character hammering shingles on a sloped roof">
    <defs>
      <linearGradient id="roofTone" x1="0" y1="0" x2="1" y2="1">
        <stop offset="0" stop-color="#f4b6d6"/>
        <stop offset="0.55" stop-color="#f2cf8c"/>
        <stop offset="1" stop-color="#e9b86a"/>
      </linearGradient>
    </defs>
    <polygon points="440,60 440,257 80,257" fill="url(#roofTone)"/>
  </svg>
  <div class="partner"><span class="partner-badge"></span><span class="partner-label">PREFERRED<br>CONTRACTOR</span></div>

  <div class="call"><span class="call-label">Call Us:</span><span class="call-number">555 208 4100</span></div>
  <div class="accredit-badge"></div>
  <div class="rating-badge"></div>
</div>
</body>
</html>
```